Marta Quinlan Photography needs a unique, creative business card/logo design

I need a design for business cards/logo that is unique and creative in the industry. Simplicity is nice, so not too crowded. Something that will catch my customer's eye and remain in their memory. I am primarily a landscape photographer but will be soon may be branching into boudoir photography as well. I have attached my current card.

Industry/Entity Type

Business

Contact Information for Business Card

Marta Quinlan Photography
Phone: 0439 271 504
Email: MartaQuinlanPhotography@brivomail.net
Website: www.pagerly.net/MartaQuinlanPhotography.Aust

Logo Text

Marta Quinlan Photography

Requirements
Must have
• Contact Details on one side
Should not have
• pixelation

```html
<!DOCTYPE html>
<html lang="en">
<head>
<meta charset="utf-8">
<title>Marta Quinlan Photography — Business Card</title>
<link href="https://fonts.googleapis.com/css2?family=Roboto+Condensed:wght@300;400&display=swap" rel="stylesheet">
<style>
  :root {
    --backdrop: #ececec;
    --paper: #ffffff;
    --panel: #f6f6f6;
    --ink: #111111;
    --type: #3a3a3a;
    --type-soft: #5a5a5a;
    --rule: #1a1a1a;
  }
  * { box-sizing: border-box; margin: 0; padding: 0; }
  html, body {
    width: 1200px;
    height: 800px;
    overflow: hidden;
    background: var(--backdrop);
  }
  .canvas {
    position: relative;
    width: 1200px;
    height: 800px;
    display: flex;
    align-items: center;
    justify-content: center;
    gap: 60px;
  }
  .card {
    position: relative;
    width: 520px;
    height: 297px;
    box-shadow: 0 2px 6px rgba(0,0,0,0.12);
  }

  /* Contact side */
  .card--contact { background: var(--paper); }
  .contact-frame {
    position: absolute;
    inset: 22px;
    border: 1.5px solid var(--rule);
    display: flex;
    flex-direction: column;
    align-items: center;
    justify-content: center;
    text-align: center;
    font-family: "Roboto Condensed", sans-serif;
    font-weight: 300;
    color: var(--type);
    line-height: 1.3;
  }
  .contact-name { font-size: 16px; color: var(--type-soft); }
  .contact-phone { font-size: 23px; letter-spacing: 1px; }
  .contact-email { font-size: 18px; }
  .contact-web { font-size: 17px; }

  /* Brand side */
  .card--brand { background: var(--ink); }
  .brand-line {
    position: absolute;
    inset: 16px;
    border: 2px solid var(--paper);
  }
  .brand-panel {
    position: absolute;
    inset: 24px;
    background: var(--panel);
    display: flex;
    flex-direction: column;
    justify-content: center;
    padding-left: 110px;
  }
  .brand-name {
    font-family: "Roboto Condensed", sans-serif;
    font-weight: 300;
    font-size: 27px;
    letter-spacing: 7px;
    line-height: 1.15;
    color: var(--type-soft);
    text-transform: uppercase;
  }
</style>
</head>
<body>
  <main class="canvas">
    <section class="card card--contact" aria-label="Contact side">
      <div class="contact-frame">
        <p class="contact-name">Marta Quinlan Photography</p>
        <p class="contact-phone">0439 271 504</p>
        <p class="contact-email">MartaQuinlanPhotography@brivomail.net</p>
        <p class="contact-web">www.pagerly.net/MartaQuinlanPhotography.Aust</p>
      </div>
    </section>

    <section class="card card--brand" aria-label="Brand side">
      <div class="brand-line"></div>
      <div class="brand-panel">
        <h1 class="brand-name">Marta Quinlan<br>Photography</h1>
      </div>
    </section>
  </main>
</body>
</html>
```